Business Card for Mortuary

We need a business card design for our mortuary. We are not the "traditional" mortuary and specialize in simple cremations and burials. We use a two sided card.

Industry/Entity Type

Funeral Home

Contact Information for Business Card

One side we would like to have with the general information of the mortuary:
Address: 4127 E. Larkspur Ave, Sun City, AZ 85399
Phone: 623-555-0142
email: hello@willowbendmortuary.example
website: willowbendmortuary.example

On the other side would like to have the information of employee:
Name: Mark T. Ellis
Email: mark@willowbendmortuary.example
Title: Funeral Director
Text: 602-555-0187

Font styles to use
Serif
Sans Serif

Requirements
Should not have
• Do not put any gothic images or things like a hearse or tombstone.

```html
<!DOCTYPE html>
<html lang="en">
<head>
<meta charset="utf-8">
<title>Willowbend Mortuary – Business Cards</title>
<link href="https://fonts.googleapis.com/css2?family=Lato:wght@400;700&display=swap" rel="stylesheet">
<style>
  :root {
    --bg: #d1d2cd;
    --card: #ffffff;
    --green: #7cc242;
    --green-dark: #5aa82e;
    --ink: #1a1a1a;
    --navy: #1f2a5c;
  }
  * { box-sizing: border-box; margin: 0; padding: 0; }
  html, body { width: 1200px; height: 801px; overflow: hidden; }
  body {
    background: var(--bg);
    font-family: "Lato", sans-serif;
    position: relative;
  }
  .card {
    position: absolute;
    width: 540px;
    height: 309px;
    background: var(--card);
    border-bottom: 5px solid var(--green);
    box-shadow: 0 14px 28px rgba(0,0,0,0.22);
  }
  .card--employee { left: 40px; top: 246px; }
  .card--company  { left: 620px; top: 246px; }

  .brand {
    position: absolute;
    display: flex;
    align-items: center;
    gap: 10px;
  }
  .brand__dot {
    width: 30px; height: 30px; border-radius: 50%;
    background: var(--green);
  }
  .brand__name {
    font-weight: 700;
    font-size: 19px;
    line-height: 1;
    color: var(--ink);
    text-transform: uppercase;
    letter-spacing: 0.5px;
  }
  .brand__tagline {
    border-left: 1px solid var(--green);
    padding-left: 6px;
    font-size: 10.5px;
    line-height: 1.15;
    color: var(--green);
  }
  .card--employee .brand { left: 34px; top: 120px; }
  .card--company .brand { right: 30px; top: 58px; }

  .person {
    position: absolute;
    right: 34px; top: 30px;
    text-align: right;
  }
  .person__name {
    font-weight: 700;
    font-size: 28px;
    color: var(--green);
  }
  .person__title {
    font-size: 14px;
    color: var(--ink);
    margin-top: 2px;
  }

  .divider {
    position: absolute;
    height: 1px;
    background: var(--green);
  }
  .card--employee .divider { left: 34px; right: 34px; top: 200px; }
  .card--company .divider { left: 34px; right: 34px; top: 186px; }

  .contacts {
    position: absolute;
    left: 34px;
    list-style: none;
  }
  .card--employee .contacts { top: 214px; }
  .card--company .contacts { top: 204px; }
  .contacts li {
    display: flex;
    align-items: center;
    gap: 14px;
    font-size: 15px;
    line-height: 26px;
  }
  .card--employee .contacts li { color: var(--ink); }
  .card--company .contacts li { color: var(--navy); }
  .icon { width: 14px; height: 14px; flex: none; }

  .address {
    position: absolute;
    right: 34px; top: 214px;
    text-align: right;
    font-style: normal;
    font-size: 15px;
    line-height: 22px;
    color: var(--navy);
  }
</style>
</head>
<body>

<section class="card card--employee">
  <div class="person">
    <div class="person__name">Mark T. Ellis</div>
    <div class="person__title">Funeral Director</div>
  </div>
  <div class="brand">
    <span class="brand__dot"></span>
    <span class="brand__name">Willowbend<br>Mortuary</span>
    <span class="brand__tagline">Affordable<br>Cremation<br>and Burial</span>
  </div>
  <div class="divider"></div>
  <ul class="contacts">
    <li><svg class="icon" viewBox="0 0 16 16"><path fill="var(--green)" d="M3 1l3 3-1.5 2a9 9 0 0 0 5.5 5.5L12 10l3 3-2 2C7 15 1 9 1 3z"/></svg>602-555-0187</li>
    <li><svg class="icon" viewBox="0 0 16 16"><rect x="1" y="3" width="14" height="10" fill="var(--green)"/><path d="M1 3l7 6 7-6" stroke="#fff" stroke-width="1.2" fill="none"/></svg>mark@willowbendmortuary.example</li>
    <li><svg class="icon" viewBox="0 0 16 16"><g fill="none" stroke="var(--green)" stroke-width="1.3"><circle cx="8" cy="8" r="6.5"/><ellipse cx="8" cy="8" rx="3" ry="6.5"/><path d="M1.5 8h13M2.5 5h11M2.5 11h11"/></g></svg>www.willowbendmortuary.example</li>
  </ul>
</section>

<section class="card card--company">
  <div class="brand">
    <span class="brand__dot"></span>
    <span class="brand__name">Willowbend<br>Mortuary</span>
    <span class="brand__tagline">Affordable<br>Cremation<br>and Burial</span>
  </div>
  <div class="divider"></div>
  <ul class="contacts">
    <li><svg class="icon" viewBox="0 0 16 16"><path fill="var(--green)" d="M3 1l3 3-1.5 2a9 9 0 0 0 5.5 5.5L12 10l3 3-2 2C7 15 1 9 1 3z"/></svg>623-555-0142</li>
    <li><svg class="icon" viewBox="0 0 16 16"><rect x="1" y="3" width="14" height="10" fill="var(--green)"/><path d="M1 3l7 6 7-6" stroke="#fff" stroke-width="1.2" fill="none"/></svg>hello@willowbendmortuary.example</li>
    <li><svg class="icon" viewBox="0 0 16 16"><g fill="none" stroke="var(--green)" stroke-width="1.3"><circle cx="8" cy="8" r="6.5"/><ellipse cx="8" cy="8" rx="3" ry="6.5"/><path d="M1.5 8h13M2.5 5h11M2.5 11h11"/></g></svg>www.willowbendmortuary.example</li>
  </ul>
  <address class="address">4127 E. Larkspur Ave,<br>Sun City, AZ 85399</address>
</section>

</body>
</html>
```